Inspirational speaker and coach Corinne Valbeck is building a website

Design, Create and launch a 10-15 page Wordpress website. Please research Corinne online and use examples you have access to.

```html
<!DOCTYPE html>
<html lang="en">
<head>
<meta charset="utf-8">
<title>Corinne Valbeck — Coaching &amp; Speaking</title>
<link href="https://fonts.googleapis.com/css2?family=Playfair+Display:wght@400;700;800&family=Pinyon+Script&family=Montserrat:wght@400;500;600;700&display=swap" rel="stylesheet">
<style>
:root{
  --olive:#9d9c6b;
  --olive-dark:#87865a;
  --cream:#f2f1ea;
  --ink:#111111;
  --text:#333333;
  --muted:#6b6b6b;
  --white:#ffffff;
  --serif:"Playfair Display",Georgia,serif;
  --script:"Pinyon Script",cursive;
  --sans:"Montserrat",Arial,sans-serif;
}
*{box-sizing:border-box;margin:0;padding:0}
html,body{width:1200px;height:5367px;overflow:hidden}
body{position:relative;background:var(--white);font-family:var(--sans);color:var(--text)}
.section{position:absolute;left:0;width:1200px;overflow:hidden}
.abs{position:absolute}
.eyebrow{position:absolute;left:0;width:100%;text-align:center;font-family:var(--script);font-size:22px;color:var(--ink)}
.heading{position:absolute;left:0;width:100%;text-align:center;font-family:var(--serif);font-weight:700;font-size:22px;color:var(--ink)}
.btn{position:absolute;display:flex;align-items:center;justify-content:center;border-radius:20px;font-family:var(--sans);font-weight:700;font-size:12px;letter-spacing:.5px}
.btn-dark{background:var(--ink);color:var(--white)}
.photo{position:absolute}

/* hero */
.hero{top:0;height:638px;background:var(--olive)}
.hero-photo-bg{left:560px;top:0;width:640px;height:638px;background:#0c0c0c}
.nav{position:absolute;left:58px;top:24px;width:1084px;height:88px;background:var(--ink);display:flex;align-items:center}
.brand{position:absolute;left:30px;font-family:var(--serif);font-size:26px;font-style:normal;color:var(--white);font-weight:400}
.nav-links{position:absolute;left:382px;display:flex;gap:30px;font-size:11px;font-weight:500;color:var(--white);letter-spacing:.3px}
.nav-links .active{color:#d9d690}
.nav-btn{left:902px;top:29px;width:128px;height:38px;background:#d6d4a4;color:var(--ink)}
.hero-title{left:103px;top:252px;font-family:var(--serif);font-weight:800;font-size:38px;line-height:54px;color:var(--white)}
.hero-sub{left:103px;top:376px;font-family:var(--script);font-size:27px;line-height:30px;color:var(--ink)}
.hero-btn{left:101px;top:461px;width:128px;height:36px}

/* welcome */
.welcome{top:638px;height:758px;background:var(--white)}
.welcome p{position:absolute;left:330px;width:540px;text-align:center;font-size:12px;line-height:18px;color:var(--muted)}
.signature{left:0;width:100%;text-align:center;top:303px;font-family:var(--serif);font-size:24px;color:var(--ink)}

/* coaching */
.coaching{top:1396px;height:510px;background:var(--cream)}
.price-card{left:244px;top:256px;width:183px;height:177px;background:var(--white);box-shadow:0 2px 10px rgba(0,0,0,.15);padding:16px 14px}
.price-card h4{font-family:var(--serif);font-size:15px;font-weight:700;color:var(--ink);margin-bottom:14px}
.price-row{display:flex;justify-content:space-between;font-size:11px;color:var(--text);padding:7px 4px;border-top:1px solid #e4e4e4}
.topic-title{left:621px;top:203px;font-family:var(--serif);font-size:30px;color:var(--ink)}
.topic-text{left:621px;top:268px;width:385px;font-size:11.5px;line-height:19px;color:var(--muted)}

/* courses */
.courses{top:1906px;height:590px;background:var(--white)}
.course-card{position:absolute;top:159px;width:253px;height:298px}
.course-tag{position:absolute;left:18px;top:0;width:56px;height:278px;background:var(--olive);display:flex;align-items:flex-end;justify-content:center;padding-bottom:18px}
.course-tag span{writing-mode:vertical-rl;transform:rotate(180deg);color:var(--white);font-size:20px;font-weight:500}
.course-feature{position:absolute;left:0;top:0;width:253px;height:298px;background:var(--olive);padding:24px 40px 0 40px;color:var(--white)}
.course-feature h5{font-size:16px;font-weight:500;margin-bottom:8px}
.course-feature p{font-size:11.5px;line-height:17px}
.dots{position:absolute;top:2403px;left:0}

/* events */
.events{top:2496px;height:414px;background:var(--cream)}
.events-sub{left:60px;top:130px;width:420px;font-size:18px;line-height:28px;color:var(--ink);font-weight:500}
.events-text{left:60px;top:192px;width:410px;font-size:11.5px;line-height:19px;color:var(--muted)}

/* team */
.team{top:2910px;height:548px;background:var(--white)}
.member{position:absolute;top:188px;width:260px;text-align:center}
.member-name{margin-top:213px;font-size:18px;color:var(--ink)}
.member-role{margin-top:6px;font-size:11px;color:var(--olive)}
.member-phone{margin-top:6px;font-size:11px;color:var(--text)}
.member-phone u{text-underline-offset:2px}

/* gallery */
.gallery{top:3458px;height:719px;background:var(--cream)}

/* resources */
.resources{top:4177px;height:552px;background:var(--white)}
.post{position:absolute;top:169px;width:263px}
.post-date{position:absolute;left:0;top:179px;width:150px;height:33px;background:var(--olive);color:var(--white);font-size:11px;display:flex;align-items:center;padding-left:12px}
.post h5{position:absolute;left:10px;top:253px;font-size:18px;font-weight:500;color:var(--ink)}
.post p{position:absolute;left:10px;top:281px;width:240px;font-size:11.5px;line-height:19px;color:var(--muted)}

/* contact */
.contact{top:4729px;height:375px;background:#1d1d1b}
.contact h3{position:absolute;top:72px;font-family:var(--serif);font-weight:700;font-size:22px;color:var(--white)}
.contact-item{position:absolute;left:121px;display:flex;gap:22px;font-size:11.5px;line-height:18px;color:#e0e0e0}
.contact-item svg{flex:none;margin-top:1px}
.field{position:absolute;background:var(--white);border:1px solid #ccc;font-size:11px;color:#666;padding:9px 10px}
.send-btn{left:504px;top:267px;width:160px;height:35px;background:var(--olive);color:var(--white)}

/* footer */
.footer{top:5104px;height:263px;background:var(--olive)}
.footer-brand{left:0;width:100%;text-align:center;top:42px;font-family:var(--serif);font-size:28px;color:var(--white)}
.footer-nav{left:0;width:100%;top:101px;display:flex;justify-content:center;gap:18px;font-size:11.5px;color:var(--white)}
.footer-nav .sep{opacity:.8}
.socials{left:0;width:100%;top:155px;display:flex;justify-content:center;gap:10px}
.socials span{width:24px;height:24px;border:1.5px solid var(--white);border-radius:50%}
.copyright{left:0;width:100%;top:213px;text-align:center;font-size:11px;color:var(--white)}
</style>
</head>
<body>

<!-- HERO -->
<section class="section hero">
  <div class="abs hero-photo-bg"></div>
  <svg class="photo" style="left:0;top:0" width="1200" height="638" role="img" aria-label="Portrait of the coach with long platinum hair, smiling">
    <defs>
      <linearGradient id="heroG" x1="0" y1="0" x2="1" y2="1">
        <stop offset="0" stop-color="#b9b8a6"/>
        <stop offset=".5" stop-color="#8f8e84"/>
        <stop offset="1" stop-color="#3b3a35"/>
      </linearGradient>
    </defs>
    <path d="M720 60 C 840 40, 1060 60, 1140 90 L1170 638 L610 638 C 560 520, 600 380, 650 260 C 680 180, 700 110, 720 60 Z" fill="url(#heroG)"/>
    <path d="M440 0 L560 0 L560 110 C 500 80, 470 40, 440 0 Z" fill="#b7b68a"/>
  </svg>
  <nav class="nav">
    <span class="brand">Corinne Valbeck</span>
    <div class="nav-links">
      <span class="active">HOME</span><span>ABOUT ME</span><span>COACHING</span><span>COURSES</span><span>EVENTS</span><span>RESOURCES</span>
    </div>
    <div class="btn nav-btn">VIEW ONLINE</div>
  </nav>
  <h1 class="abs hero-title">You Will Inspire Others<br>With Your Journey !</h1>
  <div class="abs hero-sub">Don't Be Afraid To Start From<br>Scratch !</div>
  <div class="btn btn-dark hero-btn">VIEW ONLINE</div>
</section>

<!-- WELCOME -->
<section class="section welcome">
  <div class="eyebrow" style="top:82px">Welcome To</div>
  <h2 class="heading" style="top:117px">Welcome &nbsp;To Corinne Valbeck</h2>
  <p style="top:166px">I am an experienced and seasoned business executive with expertise in operations, administration and management for multimillion-dollar companies</p>
  <p style="top:212px">I possess a strong strategic vision with ability to pinpoint and resolve complex dynamic problems. I am particularly focused on organizational structure and believe in helping employees and executives realize their full potential. I have a proven track record of sustainably growing company revenue and business development.</p>
  <div class="abs signature">Corinne Valbeck</div>
  <div class="photo" style="left:194px;top:372px;width:189px;height:313px;background:linear-gradient(160deg,#8a8a8a,#2c2c2c)" role="img" aria-label="Black and white photo of the coach holding a hat"></div>
  <div class="photo" style="left:404px;top:372px;width:390px;height:313px;background:linear-gradient(160deg,#7e7240,#c2a868 55%,#3a3422)" role="img" aria-label="Photo of the coach in a patterned jacket"></div>
  <div class="photo" style="left:817px;top:372px;width:187px;height:313px;background:linear-gradient(170deg,#9a8d86,#3a2a28)" role="img" aria-label="Photo of the coach in a dark feathered top"></div>
</section>

<!-- COACHING -->
<section class="section coaching">
  <div class="eyebrow" style="top:70px">Coaching</div>
  <h2 class="heading" style="top:106px">Coaching Online</h2>
  <svg class="photo" style="left:320px;top:164px" width="280" height="270" role="img" aria-label="Team working together at laptops in an office">
    <defs><linearGradient id="coachG" x1="0" y1="0" x2="1" y2="1"><stop offset="0" stop-color="#cdb89a"/><stop offset=".6" stop-color="#6d6a66"/><stop offset="1" stop-color="#2d3640"/></linearGradient></defs>
    <path d="M40 30 C 90 -5, 200 0, 250 50 C 290 95, 270 170, 220 220 C 170 265, 110 275, 85 220 C 60 170, 0 130, 5 85 C 10 55, 20 45, 40 30 Z" fill="url(#coachG)"/>
  </svg>
  <div class="abs price-card">
    <h4>Coaching Online</h4>
    <div class="price-row"><span>Individual Course</span><span>$120</span></div>
    <div class="price-row"><span>2 Lession</span><span>$100</span></div>
    <div class="price-row"><span>Course Name</span><span>$50</span></div>
    <div class="price-row"><span>Individual Course</span><span>$10</span></div>
  </div>
  <div class="abs topic-title">Marketing</div>
  <p class="abs topic-text">Lorem ipsum dolor sit amet consetetur sadipscing elitr sed diam nonumy eirmod tempor invidunt ut labore et dolore magna aliquyam erat sed diam voluptua. At vero eos et accusam et justo duo dolores et ea rebum. Stet clita kasd gubergren, no sea takimata sanctus est Lorem ipsum dolor sit amet.</p>
  <svg class="abs" style="left:104px;top:281px" width="62" height="38" aria-hidden="true">
    <circle cx="40" cy="19" r="17" fill="none" stroke="#222" stroke-width="1.5"/>
    <path d="M52 19 H4 M10 14 L4 19 L10 24" fill="none" stroke="#222" stroke-width="1.5"/>
  </svg>
  <svg class="abs" style="left:1058px;top:281px" width="62" height="38" aria-hidden="true">
    <circle cx="22" cy="19" r="17" fill="none" stroke="#c9c8a3" stroke-width="1.5"/>
    <path d="M10 19 H58 M52 14 L58 19 L52 24" fill="none" stroke="#c9c8a3" stroke-width="1.5"/>
  </svg>
</section>

<!-- COURSES -->
<section class="section courses">
  <div class="eyebrow" style="top:75px">New Courses</div>
  <h2 class="heading" style="top:112px">Courses</h2>
  <div class="course-card" style="left:60px;background:linear-gradient(150deg,#c9c3b6,#6a5d4f)" role="img" aria-label="Desk with laptop and photographs">
    <div class="course-tag"><span>Business</span></div>
  </div>
  <div class="course-card" style="left:337px;background:linear-gradient(150deg,#9fb1bd,#4d5e66)" role="img" aria-label="Two men talking at a table by a window">
    <div class="course-tag"><span>Construction</span></div>
  </div>
  <div class="course-card" style="left:610px">
    <div class="course-feature">
      <h5>Growing Company</h5>
      <p>Lorem ipsum dolor sit amet consetetur sadipscing elitr sed diam nonumy eirmod tempor invidunt</p>
    </div>
    <svg class="abs" style="left:168px;top:247px" width="26" height="26" aria-hidden="true">
      <circle cx="13" cy="13" r="12" fill="#fff"/><path d="M11 8 L16 13 L11 18" fill="none" stroke="#555" stroke-width="1.6"/>
    </svg>
  </div>
  <div class="course-card" style="left:887px;background:linear-gradient(150deg,#b57a5c,#3a4a66)" role="img" aria-label="Woman working at a laptop">
    <div class="course-tag" style="left:18px"><span>Marketing</span></div>
  </div>
  <svg class="abs" style="left:552px;top:491px" width="96" height="24" aria-hidden="true">
    <g fill="none" stroke="#333" stroke-width="1.2">
      <circle cx="8" cy="12" r="5"/><circle cx="24" cy="12" r="5"/><circle cx="72" cy="12" r="5"/><circle cx="88" cy="12" r="5"/>
    </g>
    <circle cx="48" cy="12" r="9" fill="none" stroke="var(--olive)" stroke-width="2"/>
  </svg>
</section>

<!-- EVENTS -->
<section class="section events">
  <div class="abs" style="left:60px;top:66px;font-family:var(--script);font-size:22px;color:var(--ink)">Blog</div>
  <h2 class="abs" style="left:60px;top:96px;font-family:var(--serif);font-weight:700;font-size:22px;color:var(--ink)">Events</h2>
  <p class="abs events-sub">Lorem Ipsum is simply dummy text of the printing and typesetting industry.</p>
  <p class="abs events-text">It is a long established fact that a reader will be distracted by the readable content of a page when looking at its layout. The point of using Lorem Ipsum is that it has a more-or-less normal distribution of letters, as opposed to using 'Content here, content here', making it look like readable English.</p>
  <div class="btn btn-dark" style="left:60px;top:314px;width:128px;height:36px">VIEW ALL</div>
  <svg class="photo" style="left:620px;top:-20px" width="480" height="460" role="img" aria-label="Two women discussing ideas in a bright office">
    <defs><linearGradient id="eventG" x1="0" y1="0" x2="1" y2="1"><stop offset="0" stop-color="#3d5a7a"/><stop offset=".5" stop-color="#b68a72"/><stop offset="1" stop-color="#e6e2de"/></linearGradient></defs>
    <path d="M40 60 C 120 -5, 330 0, 420 40 C 480 70, 470 190, 430 270 C 390 350, 260 460, 170 430 C 90 400, 30 330, 15 240 C 0 160, 0 100, 40 60 Z" fill="url(#eventG)"/>
    <circle cx="190" cy="342" r="32" fill="#f2f1ea" stroke="#fff" stroke-width="3"/>
    <circle cx="270" cy="350" r="32" fill="#3d4a5a" stroke="#fff" stroke-width="3"/>
    <circle cx="412" cy="346" r="32" fill="#6a6258" stroke="#fff" stroke-width="3"/>
  </svg>
</section>

<!-- TEAM -->
<section class="section team">
  <div class="eyebrow" style="top:93px">Our Team</div>
  <h2 class="heading" style="top:128px">Winning Team</h2>
  <div class="member" style="left:162px">
    <svg class="abs" style="left:32px;top:0" width="198" height="192" role="img" aria-label="Team member working on a laptop">
      <path d="M30 35 C 70 0, 170 -5, 190 30 C 205 70, 190 150, 140 180 C 95 205, 60 170, 30 150 C 0 125, -5 65, 30 35 Z" fill="#a69987"/>
    </svg>
    <div class="member-name">Maren Dulow</div>
    <div class="member-role">Co- Founder</div>
    <div class="member-phone">PHONE : <u>123 456 7890</u></div>
  </div>
  <div class="member" style="left:476px">
    <svg class="abs" style="left:32px;top:0" width="198" height="192" role="img" aria-label="Team member working at a desk">
      <path d="M30 35 C 70 0, 170 -5, 190 30 C 205 70, 190 150, 140 180 C 95 205, 60 170, 30 150 C 0 125, -5 65, 30 35 Z" fill="#c7c3bd" stroke="#ddd" stroke-width="4"/>
    </svg>
    <div class="member-name">Maren Dulow</div>
    <div class="member-role">Co- Founder</div>
    <div class="member-phone">PHONE : <u>123 456 7890</u></div>
  </div>
  <div class="member" style="left:808px">
    <svg class="abs" style="left:32px;top:0" width="198" height="192" role="img" aria-label="Team member standing by a blue wall">
      <path d="M30 35 C 70 0, 170 -5, 190 30 C 205 70, 190 150, 140 180 C 95 205, 60 170, 30 150 C 0 125, -5 65, 30 35 Z" fill="#2e5f8c"/>
    </svg>
    <div class="member-name">Maren Dulow</div>
    <div class="member-role">Co- Founder</div>
    <div class="member-phone">PHONE : <u>123 456 7890</u></div>
  </div>
</section>

<!-- GALLERY -->
<section class="section gallery">
  <div class="eyebrow" style="top:72px">Resources</div>
  <h2 class="heading" style="top:104px">Gallery</h2>
  <div class="photo" style="left:271px;top:136px;width:225px;height:156px;background:linear-gradient(150deg,#3b2a55,#7a4a70)" role="img" aria-label="Event poster for a leadership gathering"></div>
  <div class="photo" style="left:519px;top:136px;width:225px;height:156px;background:linear-gradient(150deg,#d8dadb,#6d7c88)" role="img" aria-label="Colleagues reviewing documents"></div>
  <div class="photo" style="left:767px;top:136px;width:225px;height:156px;background:linear-gradient(150deg,#4a4238,#c8b6a0)" role="img" aria-label="Close portrait of the coach"></div>
  <div class="photo" style="left:271px;top:315px;width:225px;height:160px;background:linear-gradient(150deg,#9a9a9a,#262626)" role="img" aria-label="Black and white photo of the coach with a horse"></div>
  <div class="photo" style="left:519px;top:315px;width:225px;height:160px;background:linear-gradient(180deg,#3d3b4a,#c46a45 60%,#2a1e1c)" role="img" aria-label="Person on a hilltop at sunset"></div>
  <div class="photo" style="left:767px;top:315px;width:225px;height:340px;background:linear-gradient(160deg,#c7c9cc,#4a4440)" role="img" aria-label="Two women sharing a conversation"></div>
  <div class="photo" style="left:271px;top:498px;width:225px;height:157px;background:linear-gradient(170deg,#b7c3cc,#b6a690)" role="img" aria-label="The coach on a beach in a cap"></div>
  <div class="photo" style="left:519px;top:498px;width:225px;height:157px;background:linear-gradient(160deg,#e8e2d4,#c8a040 60%,#4a4a4a)" role="img" aria-label="Team meeting in a creative studio"></div>
</section>

<!-- RESOURCES -->
<section class="section resources">
  <div class="eyebrow" style="top:74px">News</div>
  <h2 class="heading" style="top:108px">Resources</h2>
  <article class="post" style="left:177px">
    <div class="photo" style="left:0;top:0;width:263px;height:216px;background:linear-gradient(160deg,#e6dccb,#8a6a48 60%,#2d2a28)" role="img" aria-label="Team working in a shared office"></div>
    <div class="post-date">Aug 12 ,2021</div>
    <h5>Business</h5>
    <p>Lorem Ipsum is simply dummy text of the printing and typesetting .</p>
  </article>
  <article class="post" style="left:469px">
    <div class="photo" style="left:0;top:0;width:263px;height:216px;background:linear-gradient(160deg,#d9d8d2,#8e8b80 60%,#3a3632)" role="img" aria-label="Two women talking at a table"></div>
    <div class="post-date">Aug 12 ,2021</div>
    <h5>Consulting</h5>
    <p>Lorem Ipsum is simply dummy text of the printing and typesetting .</p>
  </article>
  <article class="post" style="left:760px">
    <div class="photo" style="left:0;top:0;width:263px;height:216px;background:linear-gradient(160deg,#c79a7a,#6d7fa0 60%,#3a3a3a)" role="img" aria-label="Two colleagues discussing at a laptop"></div>
    <div class="post-date">Aug 12 ,2021</div>
    <h5>Marketing</h5>
    <p>Lorem Ipsum is simply dummy text of the printing and typesetting .</p>
  </article>
</section>

<!-- CONTACT -->
<section class="section contact">
  <div class="photo" style="left:0;top:0;width:1200px;height:375px;background:linear-gradient(120deg,#2b2b28,#151514 50%,#2a2822)" role="img" aria-label="Dimmed photo of people at a busy event"></div>
  <h3 style="left:121px">Contact US</h3>
  <div class="contact-item" style="top:115px">
    <svg width="14" height="14" viewBox="0 0 24 24" aria-hidden="true"><path d="M6.6 10.8a15.1 15.1 0 0 0 6.6 6.6l2.2-2.2c.3-.3.7-.4 1-.2 1.1.4 2.3.6 3.6.6.6 0 1 .4 1 1V20c0 .6-.4 1-1 1C10.6 21 3 13.4 3 4c0-.6.4-1 1-1h3.5c.6 0 1 .4 1 1 0 1.3.2 2.5.6 3.6.1.3 0 .7-.2 1z" fill="#fff"/></svg>
    <span>123 456 7890</span>
  </div>
  <div class="contact-item" style="top:168px">
    <svg width="14" height="12" viewBox="0 0 24 18" aria-hidden="true"><rect x="1" y="1" width="22" height="16" fill="none" stroke="#fff" stroke-width="2"/><path d="M1 1 L12 10 L23 1" fill="none" stroke="#fff" stroke-width="2"/></svg>
    <span>info@corinnevalbeck.com</span>
  </div>
  <div class="contact-item" style="top:220px">
    <svg width="14" height="16" viewBox="0 0 24 28" aria-hidden="true"><path d="M12 1a9 9 0 0 0-9 9c0 7 9 17 9 17s9-10 9-17a9 9 0 0 0-9-9z" fill="none" stroke="#fff" stroke-width="2"/><circle cx="12" cy="10" r="3" fill="#fff"/></svg>
    <span>101- Lorem Ipsum Is<br>dummy Printing</span>
  </div>
  <h3 style="left:504px">Keep In Touch</h3>
  <div class="field" style="left:504px;top:115px;width:271px;height:36px">Name :</div>
  <div class="field" style="left:796px;top:115px;width:271px;height:36px">Email :</div>
  <div class="field" style="left:504px;top:167px;width:563px;height:80px">Name :</div>
  <div class="btn send-btn">SEND MESSAGE</div>
</section>

<!-- FOOTER -->
<footer class="section footer">
  <div class="abs footer-brand">Corinne Valbeck</div>
  <nav class="abs footer-nav">
    <span>Home</span><span class="sep">|</span><span>About Me</span><span class="sep">|</span><span>Courses</span><span class="sep">|</span><span>Coaching</span><span class="sep">|</span><span>Events</span><span class="sep">|</span><span>Resources</span><span class="sep">|</span><span>Contact Us</span>
  </nav>
  <div class="abs socials" aria-label="Social profiles"><span></span><span></span><span></span><span></span></div>
  <div class="abs copyright">© Copyright Corinne Valbeck - All Right Reserved</div>
</footer>

</body>
</html>
```